Website Design for a Law Firm

We require a fully functional Website that will be added features such as live chat, Online payment system and online forms. We need to be able to edit the website and update it regularly. We have made a website structure that is attached below.

The website footer must have:
Liability limited by a Scheme approved under Professional Standards Legislation. All legal practitioners employed by Brantley Lawyers Pty Limited (including those described as Principal Solicitor) are members of the Scheme.

Target Market(s)

People seeking legal services in Australia

Industry/Entity Type

Legal

Coding

Coded - Design and coding required

Number of Pages Required

1 page

Requirements
Must have
• Online portal function where clients can upload documents; website that would work perfectly on standard mobile, tablet, laptop, and desktop sizes; the website must have an online payment system.
Nice to have
• Online portal function where clients

```html
<!DOCTYPE html>
<html lang="en">
<head>
<meta charset="utf-8">
<title>Brantley Lawyers</title>
<link href="https://fonts.googleapis.com/css2?family=Cinzel:wght@600;700&family=Roboto:wght@400;500;700&display=swap" rel="stylesheet">
<style>
:root{
  --gold:#c9a050;
  --green:#0c2a1e;
  --cream:#f8f3e6;
  --ink:#1d1d1d;
  --grey:#777;
  --footer:#222222;
  --white:#ffffff;
}
*{box-sizing:border-box;margin:0;padding:0}
html,body{width:1200px;height:3926px;overflow:hidden}
body{position:relative;font-family:'Roboto',Arial,sans-serif;color:var(--ink);background:var(--white)}

/* header */
.site-header{position:absolute;left:0;top:0;width:1200px;height:121px;background:var(--cream)}
.nav{position:absolute;top:82px;display:flex;gap:24px;font-size:12.5px;font-weight:500;color:var(--ink);text-transform:uppercase}
.nav .active{color:var(--gold);border-bottom:2px solid var(--gold);padding-bottom:4px}
.nav-left{left:110px}
.nav-right{right:110px;gap:28px}
.brand{position:absolute;left:525px;top:30px;display:flex;align-items:center;gap:10px}
.brand-mark{width:40px;height:40px;border:2px solid var(--gold);border-radius:50%}
.brand-name{font-family:'Cinzel',Georgia,serif;font-weight:700;font-size:24px;color:var(--green);letter-spacing:1px}
.phone{position:absolute;left:889px;top:20px;display:flex;align-items:center;gap:16px;font-weight:700;font-size:17px}
.phone-ico{width:42px;height:42px;border-radius:50%;background:var(--gold);display:flex;align-items:center;justify-content:center}

/* hero */
.hero{position:absolute;left:0;top:121px;width:1200px;height:601px;
  background:linear-gradient(180deg,#8fa3a6 0%,#7d8d8c 35%,#5f7f8c 62%,#567c8a 75%,#4f6d3e 100%)}
.hero-box{position:absolute;left:283px;top:169px;width:633px;height:263px;background:rgba(70,70,70,.55);text-align:center;color:var(--white)}
.hero-box h1{font-family:'Cinzel',Georgia,serif;font-size:40px;font-weight:700;margin-top:28px}
.hero-box p{font-size:17px;line-height:29px;margin-top:12px;padding:0 40px}
.btn-gold{display:inline-block;background:var(--gold);color:var(--white);font-weight:700;font-size:13px;text-transform:uppercase}
.hero-box .btn-gold{margin-top:20px;padding:14px 22px}
.dots{position:absolute;left:566px;top:566px;display:flex;gap:12px;align-items:center}
.dots i{width:6px;height:6px;border-radius:50%;background:var(--white);display:block}
.dots i.on{width:14px;height:14px;border:2px solid var(--gold);background:transparent}

/* section titles */
.sec-mark{width:58px;height:58px;border:2px solid var(--gold);border-radius:50%}
.sec-title{font-family:'Cinzel',Georgia,serif;font-weight:700;font-size:42px;color:var(--green);letter-spacing:1px}
.sec-title span{color:var(--gold)}
.center-head{position:absolute;left:0;width:1200px;text-align:center}
.center-head .sec-mark{margin:0 auto 6px}

/* about */
.about-frame{position:absolute;left:280px;top:837px;width:277px;height:293px;border:3px solid var(--gold)}
.about-photo{position:absolute;left:110px;top:873px;width:415px;height:425px;background:var(--white);box-shadow:0 4px 14px rgba(0,0,0,.18);padding:7px}
.about-photo div{width:100%;height:100%;background:linear-gradient(135deg,#5a5651,#c9c4bd 55%,#e7e5e2)}
.about-text{position:absolute;left:608px;top:863px;width:482px}
.about-text p{font-size:13.5px;line-height:26px;color:var(--grey);text-align:justify;margin-top:12px}
.about-text .btn-gold{margin-top:34px;padding:15px 22px}

/* services */
.services{position:absolute;left:0;top:1528px;width:1200px;display:grid;grid-template-columns:repeat(4,1fr);gap:5px}
.tile{height:222px;position:relative;display:flex;align-items:center;justify-content:center;text-align:center;color:var(--white);font-weight:700;font-size:16px;text-transform:uppercase;line-height:25px}
.tile span{position:relative;z-index:1}
.tile span::after{content:"";display:block;width:40px;height:2px;background:var(--white);margin:8px auto 0}
.tile.framed::before{content:"";position:absolute;inset:10px;border:2px solid var(--white)}

/* blog */
.blog-card{position:absolute;top:2214px;width:310px}
.blog-img{height:206px}
.blog-body{padding:16px 18px 0 17px;border-right:3px solid var(--gold);height:196px;border-image:linear-gradient(180deg,var(--gold) 0 27%,#eee 27% 100%) 1}
.blog-body h3{font-size:17px;font-weight:500;line-height:25px}
.meta{font-size:12px;color:#999;margin-top:6px;display:flex;gap:22px}
.blog-body p{font-size:13px;line-height:23px;color:var(--grey);margin-top:8px}
.more{font-size:12.5px;font-weight:700;color:var(--gold);margin-top:10px;display:block}

/* form */
.form-shadow{position:absolute;left:104px;top:2730px;width:393px;height:620px;border-left:4px solid var(--gold);border-bottom:4px solid var(--gold)}
.consult{position:absolute;left:110px;top:2718px;width:393px;height:622px;background:var(--green);padding:28px 27px}
.consult h2{font-family:'Cinzel',Georgia,serif;color:var(--white);font-size:34px;line-height:45px;font-weight:700;letter-spacing:1px}
.field{border:1px solid var(--white);height:52px;margin-top:20px;color:var(--white);font-size:13.5px;font-weight:700;padding:17px 13px;position:relative}
.field.first{margin-top:24px}
.field.area{height:105px}
.field .caret{position:absolute;right:10px;top:16px;font-size:10px;line-height:9px}
.submit{margin-top:18px;height:52px;background:var(--gold);color:var(--white);font-weight:700;font-size:17px;text-align:center;line-height:52px}

/* reviews */
.reviews{position:absolute;left:528px;top:2718px;width:562px}
.reviews .sec-title{font-size:42px;line-height:48px;margin-top:8px}
.arrows{position:absolute;right:0;top:122px;display:flex;gap:18px;color:var(--gold);font-size:28px}
.review{position:relative;padding-left:74px;margin-top:26px}
.quote{position:absolute;left:0;top:2px;width:58px;height:58px;border-radius:50%;background:#f1e7d5;color:var(--gold);font-family:Georgia,serif;font-size:56px;font-weight:700;text-align:center;line-height:78px}
.review h4{font-size:20px;font-weight:500}
.stars{color:var(--gold);font-size:18px;letter-spacing:4px}
.review p{font-size:13.5px;line-height:26px;color:var(--grey);text-align:justify;margin-top:8px}
.btn-outline{display:inline-block;border:3px solid var(--gold);font-size:18px;font-weight:500;padding:15px 34px;margin-top:38px;color:var(--ink)}

/* footer */
.site-footer{position:absolute;left:0;top:3418px;width:1200px;height:508px;background:var(--footer);color:var(--white)}
.fcol{position:absolute;top:77px}
.fcol h5{color:var(--gold);font-size:19px;font-weight:700;margin-bottom:14px}
.fcol li{list-style:none;font-size:16.5px;line-height:38px}
.fcol address{font-style:normal;font-size:16.5px;line-height:29px}
.socials{display:flex;gap:18px;margin-top:16px}
.socials i{display:block;width:16px;height:16px;border-radius:50%;background:#aaa}
.liability{width:270px;margin-top:18px;font-size:11.5px;line-height:17px;color:#aaa}
.hours td{font-size:16.5px;line-height:33.5px;padding-right:28px}
.chat{position:absolute;left:1073px;top:3787px;width:64px;height:64px;border-radius:50%;background:#444;display:flex;align-items:center;justify-content:center}
.rule{position:absolute;left:45px;top:3870px;width:1110px;height:1px;background:#3a3a3a}
.copy{position:absolute;left:0;top:3898px;width:1200px;text-align:center;font-size:13px;color:var(--white)}
.copy span{color:var(--gold)}
</style>
</head>
<body>

<header class="site-header">
  <nav class="nav nav-left">
    <span class="active">Home</span><span>About Us ▾</span><span>Our Services ▾</span><span>Cost ▾</span>
  </nav>
  <div class="brand"><span class="brand-mark"></span><span class="brand-name">BRANTLEY</span></div>
  <div class="phone">
    <span class="phone-ico"><svg width="20" height="20" viewBox="0 0 24 24"><path d="M6.6 10.8a15 15 0 0 0 6.6 6.6l2.2-2.2c.3-.3.7-.4 1-.2 1.1.4 2.3.6 3.6.6.6 0 1 .4 1 1V20c0 .6-.4 1-1 1C10.6 21 3 13.4 3 4c0-.6.4-1 1-1h3.5c.6 0 1 .4 1 1 0 1.3.2 2.5.6 3.6.1.3 0 .7-.2 1z" fill="#fff"/></svg></span>
    +61 7 3014 6620
  </div>
  <nav class="nav nav-right"><span>Careers</span><span>Insights</span><span>Contact Us</span><span>Blog</span></nav>
</header>

<section class="hero" role="img" aria-label="City harbour skyline with opera house and trees">
  <div class="hero-box">
    <h1>BRANTLEY LAWYERS</h1>
    <p>We are the Solicitors &amp; Immigration Lawyers located in Brisbane,<br>Gold Coast, Melbourne, Perth &amp; Sydney</p>
    <span class="btn-gold">Get a Quote</span>
  </div>
  <div class="dots"><i></i><i class="on"></i><i></i><i></i></div>
</section>

<div class="about-frame"></div>
<div class="about-photo"><div role="img" aria-label="Two colleagues reviewing documents at a laptop"></div></div>
<section class="about-text">
  <div class="sec-mark"></div>
  <h2 class="sec-title" style="margin-top:4px">ABOUT <span>US</span></h2>
  <p style="margin-top:28px">Brantley Lawyers offers a wide range of Legal Services including: Family, Criminal, Migration and Commercial/Property Law. Liability limited by a scheme approved under professional standards legislation.</p>
  <p>We are the Solicitors &amp; Immigration Lawyers located in Brisbane, Gold Coast, Melbourne, Perth &amp; Sydney with Mr Rohan Mehta as our Principal Solicitor. In Brisbane, Brantley Lawyers is located in the heart of Brisbane City at Ashcombe Terrace within walking distance to most courts.</p>
  <span class="btn-gold">Learn More</span>
</section>

<div class="center-head" style="top:1373px">
  <div class="sec-mark"></div>
  <h2 class="sec-title">OUR <span>SERVICES</span></h2>
</div>
<section class="services">
  <div class="tile" role="img" aria-label="Signing paperwork" style="background:linear-gradient(135deg,#6b6560,#a9a39c)"><span>Administrative Law</span></div>
  <div class="tile" role="img" aria-label="Business handshake at office" style="background:linear-gradient(135deg,#3f4a50,#9b9a94)"><span>Commercial Law</span></div>
  <div class="tile framed" role="img" aria-label="Handshake over property contract" style="background:linear-gradient(135deg,#2e2a27,#6e6159)"><span>Property Law</span></div>
  <div class="tile" role="img" aria-label="Stamping a document" style="background:linear-gradient(135deg,#3a2f2a,#7d726b)"><span>Immigration Law</span></div>
  <div class="tile" role="img" aria-label="Colleagues in a meeting" style="background:linear-gradient(135deg,#4a4540,#8c7d70)"><span>Employment Law</span></div>
  <div class="tile" role="img" aria-label="Consultation at a desk" style="background:linear-gradient(135deg,#8f8a84,#c8c3bc)"><span>Family &amp;<br>Relationship Law</span></div>
  <div class="tile" role="img" aria-label="Courtroom scene" style="background:linear-gradient(135deg,#1e1a18,#7a3a20)"><span>Criminal</span></div>
  <div class="tile" role="img" aria-label="Professionals in discussion" style="background:linear-gradient(135deg,#9a9590,#d4d0cb)"><span>Professional<br>Misconduct</span></div>
</section>

<div class="center-head" style="top:2056px">
  <div class="sec-mark"></div>
  <h2 class="sec-title">LATEST <span>BLOG</span></h2>
</div>
<article class="blog-card" style="left:111px">
  <div class="blog-img" role="img" aria-label="Immigration law folder" style="background:linear-gradient(135deg,#7c8a3a,#d8c7c0 55%,#f0ecea)"></div>
  <div class="blog-body">
    <h3>Complex Migration Matters - Throughout Australia</h3>
    <div class="meta"><span>Brantley Lawyers</span><span>25 Oct 2020</span></div>
    <p>If you have problems or concerns with the migration process or with your visa, Brantley Lawyers are here to assist</p>
    <span class="more">READ MORE ➜</span>
  </div>
</article>
<article class="blog-card" style="left:445px">
  <div class="blog-img" role="img" aria-label="Meeting over documents at a table" style="background:linear-gradient(135deg,#a8a29c,#6f5c48)"></div>
  <div class="blog-body">
    <h3>We are fully operational from 18 May 2020</h3>
    <div class="meta"><span>Brantley Lawyers</span><span>15 May 2020</span></div>
    <p>Taking walk-in and face-to-face consultations maintaining social distancing guidelines.</p>
    <span class="more">READ MORE ➜</span>
  </div>
</article>
<article class="blog-card" style="left:779px">
  <div class="blog-img" role="img" aria-label="Office reception interior" style="background:linear-gradient(135deg,#6b5440,#e6e2dc)"></div>
  <div class="blog-body">
    <h3>Brantley Lawyers will<br>re-open</h3>
    <div class="meta"><span>Brantley Lawyers</span><span>30 Apr 2020</span></div>
    <p>Its offices from Monday, i.e. 04 May 2020. You can book your appointments to see our solicitors face-to-face.</p>
    <span class="more">READ MORE ➜</span>
  </div>
</article>

<div class="form-shadow"></div>
<section class="consult">
  <h2>REQUEST A FREE CONSULTANT</h2>
  <div class="field first">Full Name</div>
  <div class="field">Email Address</div>
  <div class="field">Phone No</div>
  <div class="field">Subject<span class="caret">▲<br>▼</span></div>
  <div class="field area">Message</div>
  <div class="submit">SUBMIT</div>
</section>

<section class="reviews">
  <div class="sec-mark"></div>
  <h2 class="sec-title">OUR CLIENT<br><span>REVIEWS</span></h2>
  <div class="arrows"><span style="opacity:.6">←</span><span>→</span></div>
  <div class="review">
    <div class="quote">“</div>
    <h4>Daniel R</h4>
    <div class="stars">★★★★★</div>
    <p>“ Many thanks for the friendly, competent and effective cooperation. Thanks to the good preparation of my visa applications were processed quickly and successfully. I always feel very well advised and supported. I can really recommend the Brantley Lawyers with a clear conscience..”</p>
  </div>
  <div class="review">
    <div class="quote">“</div>
    <h4>Daniel R</h4>
    <div class="stars">★★★★★</div>
    <p>“ Many thanks for the friendly, competent and effective cooperation. Thanks to the good preparation of my visa applications were processed quickly and successfully. I always feel very well advised and supported. I can really recommend the Brantley Lawyers with a clear conscience..”</p>
  </div>
  <span class="btn-outline">VIEW ALL REVIEWS</span>
</section>

<footer class="site-footer">
  <div class="fcol" style="left:113px">
    <h5>SITE MAP</h5>
    <ul><li>Home</li><li>About Us</li><li>Our Services</li><li>Insights &amp; News</li><li>Careers</li><li>Costs</li><li>Blog</li><li>Contact Us</li></ul>
  </div>
  <div class="fcol" style="left:324px">
    <h5>SERVICES</h5>
    <ul><li>Administrative Law</li><li>Commercial Law</li><li>Property Law</li><li>Immigration Law</li><li>Employment Law</li><li>Family &amp; Relationship Law</li><li>Criminal</li><li>Professional Misconduct</li></ul>
  </div>
  <div class="fcol" style="left:602px">
    <h5>CONTACT INFO</h5>
    <address>Level 3/48 Ashcombe<br>Terrace Spring Hill QLD 4000<br>Australia<br><span style="line-height:38px">(07) 3014 6620</span><br>hello@brantleylawyers.example</address>
    <div class="socials"><i></i><i></i><i></i><i></i><i></i></div>
    <p class="liability">Liability limited by a Scheme approved under Professional Standards Legislation. All legal practitioners employed by Brantley Lawyers Pty Limited (including those described as Principal Solicitor) are members of the Scheme.</p>
  </div>
  <div class="fcol" style="left:893px">
    <h5>HOURS</h5>
    <table class="hours">
      <tr><td>Mon:</td><td>8:30AM – 5:00PM</td></tr>
      <tr><td>Tue:</td><td>8:30AM – 5:00PM</td></tr>
      <tr><td>Wed:</td><td>8:30AM – 5:00PM</td></tr>
      <tr><td>Thu:</td><td>8:30AM – 5:00PM</td></tr>
      <tr><td>Fri:</td><td>8:30AM – 5:00PM</td></tr>
      <tr><td>Sat:</td><td>Closed</td></tr>
      <tr><td>Sun:</td><td>Closed</td></tr>
    </table>
  </div>
</footer>
<div class="chat"><svg width="34" height="30" viewBox="0 0 34 30"><rect x="2" y="2" width="30" height="20" rx="3" fill="#fff"/><path d="M8 22 L6 29 L14 22z" fill="#fff"/><circle cx="11" cy="12" r="2" fill="#444"/><circle cx="17" cy="12" r="2" fill="#444"/><circle cx="23" cy="12" r="2" fill="#444"/></svg></div>
<div class="rule"></div>
<div class="copy">Copyright © 2023. Brantley Lawyers.All Right Reserved. &nbsp;<span>Compliance &amp; Disclaimers</span> &nbsp;|&nbsp; <span>Pay Online</span> &nbsp;|&nbsp; <span>Client Portal – Upload Documents</span></div>

</body>
</html>
```